New management consulting website

I need a 4-5 page website that I can manage in WordPress on Sitehaven.example for a new management consulting company. The website is www.tolvira.example and the company name is Tolvira Group LLC. The attached spec has an example of a draft site, layout and actual copy and includes company and contact information. I have more high-res images I can send.

Must include instruction/assistance loading the site to my WordPress dashboard.

Target Market(s)

Any business, especially SAAS

Industry/Entity Type

Consultant

Coding

Coded - Design and coding required

Number of Pages Required

4 page

Font styles to use
Sans Serif

Colors
0456a4

Requirements
Must have
• Modern and stylish

```html
<!DOCTYPE html>
<html lang="en">
<head>
<meta charset="utf-8">
<title>Tolvira Consulting</title>
<link href="https://fonts.googleapis.com/css2?family=Michroma&family=Roboto:wght@400;500;700&display=swap" rel="stylesheet">
<style>
:root{
  --navy:#1d3f6e;
  --navy-dark:#14284a;
  --orange:#f7960f;
  --ink:#222;
  --muted:#444;
  --beige:#f2ece4;
  --footer:#000;
}
*{box-sizing:border-box;margin:0;padding:0}
html,body{width:1200px;height:3941px;overflow:hidden}
body{position:relative;font-family:'Roboto',sans-serif;color:var(--ink);background:#fff}
.abs{position:absolute}
.display{font-family:'Michroma',sans-serif;font-weight:400;letter-spacing:0}
.btn{position:absolute;display:flex;align-items:center;justify-content:center;background:var(--navy);color:#fff;font:500 13px 'Roboto',sans-serif;border-radius:8px;text-transform:uppercase}
.rule{position:absolute;height:4px;background:var(--navy)}
.body-copy{position:absolute;font-size:13px;line-height:22px;color:var(--muted);text-align:justify}
.center-copy{position:absolute;font-size:13px;line-height:25px;color:var(--muted);text-align:center}

/* header */
.site-header{position:absolute;left:0;top:0;width:1200px;height:140px;background:#fff}
.brand{position:absolute;left:115px;top:42px;font:700 46px/54px 'Roboto',sans-serif;color:var(--navy);letter-spacing:2px}
.topbar{position:absolute;top:30px;right:120px;display:flex;gap:22px;font-size:12.5px;color:#444;align-items:center}
.topbar span{display:flex;align-items:center;gap:6px}
.main-nav{position:absolute;left:612px;top:88px;width:588px;height:52px;background:var(--navy-dark);clip-path:polygon(40px 0,100% 0,100% 100%,0 100%)}
.main-nav .active{position:absolute;left:30px;top:0;width:90px;height:52px;background:var(--navy);clip-path:polygon(30px 0,100% 0,100% 100%,0 100%)}
.main-nav ul{position:absolute;left:52px;top:0;height:52px;display:flex;list-style:none;gap:34px;align-items:center;color:#fff;font:500 13px 'Roboto',sans-serif}
.header-line{position:absolute;left:0;top:136px;width:612px;height:4px;background:var(--navy-dark)}

/* hero */
.hero{position:absolute;left:0;top:140px;width:1200px;height:567px;background:linear-gradient(180deg,#c9c0b0 0%,#a9b3bd 35%,#7a93ad 65%,#4d6b8c 100%)}
.hero-rock{position:absolute;right:0;top:140px;width:620px;height:567px;background:linear-gradient(120deg,rgba(20,20,24,0) 30%,#121316 60%)}
.hero-title{position:absolute;left:112px;top:236px;font-size:46px;line-height:66px;white-space:nowrap}
.hero-title .t1{color:var(--navy)}
.hero-title .t2{color:#111}
.hero-copy{position:absolute;left:112px;top:382px;font-size:16.5px;line-height:21px;color:#222}

/* intro */
.intro-card{position:absolute;left:118px;top:677px;width:964px;height:120px;background:#fff;border-radius:60px 60px 0 0}
.section-title{position:absolute;left:0;width:1200px;text-align:center;font-size:31px;line-height:44px;color:#111;white-space:nowrap}
.feature-label{position:absolute;width:226px;text-align:center}
.feature-label h3{font:700 16px 'Roboto',sans-serif;color:#111;margin-bottom:6px}
.feature-label p{font-size:12px;line-height:18px;color:#333}

/* services */
.services{position:absolute;left:0;top:1212px;width:1200px;height:1458px;background:var(--beige)}
.svc-title{position:absolute;font-size:20px;line-height:30px;color:#111;white-space:nowrap}
.photo{position:absolute;border-radius:14px}

/* team */
.team-frame{position:absolute;left:233px;top:2882px;width:262px;height:258px}
.member-name{position:absolute;left:648px;top:2877px;width:400px;text-align:center;font:500 20px 'Roboto',sans-serif;color:#111}
.member-role{position:absolute;left:648px;top:2920px;width:400px;text-align:center;font:500 15px 'Roboto',sans-serif;color:#111}

/* origins */
.origins{position:absolute;left:0;top:3205px;width:1200px;height:395px;background:linear-gradient(180deg,#3f5a7f,#2d4a70 60%,#4b6484)}
.origin-tile{position:absolute;top:3377px;width:228px;height:160px}

/* footer */
.site-footer{position:absolute;left:0;top:3600px;width:1200px;height:341px;background:var(--footer);color:#fff}
.footer-brand{position:absolute;left:185px;top:74px;font:700 34px/40px 'Roboto',sans-serif;letter-spacing:2px}
.footer-contact{position:absolute;left:185px;top:152px;font:500 12px 'Roboto',sans-serif;line-height:25px}
.footer-col-title{position:absolute;font:500 20px 'Roboto',sans-serif}
.footer-links{position:absolute;left:440px;top:133px;list-style:none;font:500 12px 'Roboto',sans-serif;line-height:25px}
.newsletter-form{position:absolute;left:662px;top:144px;display:flex}
.newsletter-form .field{width:276px;height:42px;background:#fff;color:#555;font-size:13px;padding:13px 14px}
.newsletter-form .submit{width:112px;height:42px;background:var(--navy);font:700 13px 'Roboto',sans-serif;display:flex;align-items:center;justify-content:center}
.social{position:absolute;left:662px;top:214px;display:flex;gap:9px}
.social span{width:38px;height:38px;border:2.5px solid #fff;border-radius:50%}
.copyright{position:absolute;left:0;top:300px;width:1200px;text-align:center;font-size:12px}
</style>
</head>
<body>

<header class="site-header">
  <div class="brand">TOLVIRA</div>
  <div class="topbar">
    <span><svg width="11" height="11" viewBox="0 0 24 24"><path fill="#444" d="M6.6 10.8a15 15 0 006.6 6.6l2.2-2.2c.3-.3.7-.4 1-.2 1.1.4 2.3.6 3.6.6.6 0 1 .4 1 1V20c0 .6-.4 1-1 1A17 17 0 013 4c0-.6.4-1 1-1h3.5c.6 0 1 .4 1 1 0 1.3.2 2.5.6 3.6.1.3 0 .7-.2 1z"/></svg>+1-800-555-0142</span>
    <span><svg width="12" height="10" viewBox="0 0 24 18"><rect width="24" height="18" fill="#444"/><path d="M0 0l12 9 12-9" stroke="#fff" stroke-width="2" fill="none"/></svg>support@tolvira.example</span>
    <span><svg width="12" height="10" viewBox="0 0 24 18"><rect width="24" height="18" fill="#444"/><path d="M0 0l12 9 12-9" stroke="#fff" stroke-width="2" fill="none"/></svg>Sign in</span>
    <svg width="20" height="20" viewBox="0 0 24 24"><circle cx="10" cy="10" r="7" stroke="#333" stroke-width="2" fill="none"/><path d="M15 15l7 7" stroke="#333" stroke-width="2.5"/></svg>
  </div>
  <nav class="main-nav">
    <div class="active"></div>
    <ul><li>HOME</li><li>ABOUT US</li><li>SERVICES</li><li>TEAM</li><li>CONTACT US</li></ul>
  </nav>
  <div class="header-line"></div>
</header>

<section>
  <div class="hero" role="img" aria-label="Misty blue mountain ranges at dawn"></div>
  <div class="hero-rock" role="img" aria-label="Dark cliff silhouette with two climbers helping each other to the top"></div>
  <h1 class="hero-title display"><span class="t1">TOLVIRA</span><br><span class="t2">CONSULTING</span></h1>
  <div class="hero-copy">
    <p>The Word 'Tolvira' Originates Foem old English Language.<br>it means 'above,beyond.</p>
    <p style="margin-top:22px">At Tolvira Consulting our approach is to help you rise above<br>day-to-day Tolvira Consulting</p>
  </div>
  <div class="btn" style="left:112px;top:532px;width:148px;height:48px">Learn More</div>
</section>

<section>
  <div class="intro-card"></div>
  <h2 class="section-title display" style="top:712px">TOLVIRA CONSULTING</h2>
  <div class="rule" style="left:544px;top:766px;width:112px"></div>
  <p class="center-copy" style="left:200px;top:788px;width:800px">There are many variations of passages of Lorem Ipsum available, but the majority have suffered alteration in some form, by injected humour, or randomised words which don't look even slightly believable.</p>

  <svg class="abs" style="left:0;top:850px" width="1200" height="320" viewBox="0 0 1200 320">
    <g fill="none" stroke-width="11">
      <path d="M118 155 A145 145 0 0 0 408 155" stroke="var(--orange)"/>
      <path d="M455 155 A145 145 0 0 1 745 155" stroke="var(--navy)"/>
      <path d="M792 155 A145 145 0 0 0 1082 155" stroke="var(--orange)"/>
    </g>
    <g fill="#fff" stroke="#ccc" stroke-width="1.5">
      <circle cx="263" cy="155" r="113"/>
      <circle cx="600" cy="155" r="113"/>
      <circle cx="937" cy="155" r="113"/>
    </g>
    <g transform="translate(263 95)" fill="var(--navy)">
      <circle cx="0" cy="-18" r="15"/>
      <circle cx="0" cy="-18" r="6" fill="#fff"/>
      <path d="M-34 30 Q-34 5 -12 2 L12 2 Q34 5 34 30Z"/>
    </g>
    <g transform="translate(600 95)">
      <path d="M-28 -40 h22 v18 h10 v34 h-10 v28 h-22z" fill="var(--orange)"/>
      <circle cx="8" cy="-4" r="16" fill="none" stroke="var(--orange)" stroke-width="8" stroke-dasharray="6 4"/>
    </g>
    <g transform="translate(937 95)" fill="var(--navy)">
      <rect x="-14" y="-40" width="26" height="20" rx="2"/>
      <circle cx="-26" cy="-10" r="8"/>
      <circle cx="26" cy="-10" r="8"/>
      <rect x="-36" y="2" width="12" height="30" rx="4"/>
      <rect x="24" y="2" width="12" height="30" rx="4"/>
      <rect x="-10" y="0" width="20" height="6"/>
      <rect x="-3" y="6" width="6" height="26"/>
    </g>
  </svg>
  <div class="feature-label" style="left:150px;top:1018px"><h3>Our consulting</h3><p>There are many variations<br>of passages of</p></div>
  <div class="feature-label" style="left:487px;top:1018px"><h3>Our consulting</h3><p>There are many variations<br>of passages of</p></div>
  <div class="feature-label" style="left:824px;top:1018px"><h3>Our consulting</h3><p>There are many variations<br>of passages of</p></div>
</section>

<section class="services"></section>
<h2 class="svc-title display" style="left:112px;top:1310px">STRATEGY &amp; OPERATIONS</h2>
<div class="rule" style="left:112px;top:1352px;width:90px;height:3px"></div>
<p class="body-copy" style="left:112px;top:1386px;width:432px">There are many variations of passages of Lorem Ipsum available, but the majority have suffered alteration in some form, by injected humour, or randomised words which don't look even slightly believable. If you are going to use a passage of Lorem Ipsum.</p>
<div class="btn" style="left:112px;top:1501px;width:142px;height:50px">Learn More</div>
<div class="photo" style="left:600px;top:1300px;width:488px;height:322px;background:linear-gradient(135deg,#6b6f76,#c7c2bb 50%,#4a4c52)" role="img" aria-label="Hands on a laptop with digital business icons overlay"></div>

<div class="photo" style="left:110px;top:1615px;width:488px;height:325px;background:linear-gradient(135deg,#a9d3ec,#5b9cc9 55%,#8fbcd8)" role="img" aria-label="Businessman facing a large blue data analytics display"></div>
<h2 class="svc-title display" style="left:653px;top:1666px">DATA ANALYSIS &amp; INSIGHTS</h2>
<div class="rule" style="left:653px;top:1708px;width:90px;height:3px"></div>
<p class="body-copy" style="left:653px;top:1720px;width:434px">There are many variations of passages of Lorem Ipsum available, but the majority have suffered alteration in some form, by injected humour, or randomised words which don't look even slightly believable. If you are going to use a passage of Lorem Ipsum.</p>
<div class="btn" style="left:653px;top:1834px;width:142px;height:50px">Learn More</div>

<h2 class="svc-title display" style="left:109px;top:1981px">LEADERSHIP DEVELOPMENT</h2>
<div class="rule" style="left:109px;top:2023px;width:90px;height:3px"></div>
<p class="body-copy" style="left:109px;top:2037px;width:434px">There are many variations of passages of Lorem Ipsum available, but the majority have suffered alteration in some form, by injected humour, or randomised words which don't look even slightly believable. If you are going to use a passage of Lorem Ipsum.</p>
<div class="btn" style="left:109px;top:2150px;width:142px;height:50px">Learn More</div>
<div class="photo" style="left:598px;top:1931px;width:489px;height:324px;background:linear-gradient(135deg,#8a5a40,#d9cfc2 50%,#6e7a86)" role="img" aria-label="Team discussing documents around a meeting table"></div>

<div class="photo" style="left:110px;top:2250px;width:488px;height:323px;background:linear-gradient(180deg,#dfe4ec,#b5c2d3 55%,#8aa0bb)" role="img" aria-label="Businessman silhouette blended with a city skyline"></div>
<h2 class="svc-title display" style="left:652px;top:2301px">EXECUTIVE LEADERSHIP</h2>
<div class="rule" style="left:652px;top:2343px;width:90px;height:3px"></div>
<p class="body-copy" style="left:652px;top:2356px;width:434px">There are many variations of passages of Lorem Ipsum available, but the majority have suffered alteration in some form, by injected humour, or randomised words which don't look even slightly believable. If you are going to use a passage of Lorem Ipsum.</p>
<div class="btn" style="left:652px;top:2469px;width:142px;height:50px">Learn More</div>

<section>
  <h2 class="section-title display" style="top:2708px;color:var(--navy)">OUR TEAM</h2>
  <div class="rule" style="left:544px;top:2764px;width:112px"></div>
  <p class="center-copy" style="left:270px;top:2782px;width:660px;line-height:21px">There are many variations of passages of Lorem Ipsum available, but the majority have suffered alteration in some form, by injected humour, or randomised words which</p>
  <div class="abs" style="left:598px;top:2845px;width:3px;height:290px;background:var(--navy)"></div>
  <svg class="abs" style="left:60px;top:2950px" width="1080" height="80" viewBox="0 0 1080 80">
    <path d="M48 4 L30 38 L48 72" stroke="#6a86a8" stroke-width="2" fill="none"/>
    <path d="M1030 4 L1048 38 L1030 72" stroke="#6a86a8" stroke-width="2" fill="none"/>
  </svg>
  <svg class="team-frame" viewBox="0 0 262 258">
    <g stroke="var(--navy)" stroke-width="3" fill="none">
      <path d="M60 2 H2 V60"/><path d="M202 2 H260 V60"/>
      <path d="M2 198 V256 H60"/><path d="M260 198 V256 H202"/>
    </g>
  </svg>
  <div class="abs" style="left:247px;top:2896px;width:234px;height:230px;background:linear-gradient(180deg,#eef1f4,#c9d6e6);border:1px solid #99a" role="img" aria-label="Portrait photo of a team member in a light blue shirt"></div>
  <div class="member-name">Daniel Marsh</div>
  <div class="rule" style="left:815px;top:2904px;width:66px;height:2px"></div>
  <div class="member-role">Founder and Senior Consultant</div>
  <div class="abs" style="left:780px;top:2952px;display:flex;gap:7px">
    <span style="width:28px;height:28px;border:2px solid var(--navy);border-radius:50%"></span>
    <span style="width:28px;height:28px;border:2px solid var(--navy);border-radius:50%"></span>
    <span style="width:28px;height:28px;border:2px solid var(--navy);border-radius:50%"></span>
    <span style="width:28px;height:28px;border:2px solid var(--navy);border-radius:50%"></span>
  </div>
  <p class="center-copy" style="left:648px;top:2994px;width:400px;font-size:12px;line-height:21px">There are many variations of passages of Lorem Ipsum available, but the majority have suffered alteration in some form, by injected humour, or randomised words which don't look even slightly believable.</p>
  <div class="btn" style="left:785px;top:3086px;width:126px;height:46px;border-radius:10px">View More</div>
</section>

<section class="origins" role="img" aria-label="Blue sunset sky with people raising their arms"></section>
<h2 class="section-title display" style="top:3234px;color:#fff">THE ORIGINS OF TOLVIRA</h2>
<div class="rule" style="left:544px;top:3288px;width:112px;background:#fff"></div>
<p class="center-copy" style="left:270px;top:3303px;width:660px;line-height:21px;color:#e8eef5">There are many variations of passages of Lorem Ipsum available, but the majority have suffered alteration in some form, by injected humour, or randomised words which</p>
<div class="origin-tile" style="left:112px;background:linear-gradient(135deg,#e5d07a,#7b5a2c 60%,#3d2a18)" role="img" aria-label="Hand holding soil with a green seedling"></div>
<div class="origin-tile" style="left:361px;background:linear-gradient(180deg,#b7b6a4,#6f7d4a 55%,#93a05a)" role="img" aria-label="Dog running across a park lawn"></div>
<div class="origin-tile" style="left:611px;background:linear-gradient(180deg,#3b8fe0,#4a8c3a 55%,#a4c24f)" role="img" aria-label="Green meadow with trees and a river under blue sky"></div>
<div class="origin-tile" style="left:860px;background:linear-gradient(135deg,#5a3a26,#c48a66 50%,#3a261a)" role="img" aria-label="Cupped hands holding a small plant in soil"></div>
<svg class="abs" style="left:60px;top:3420px" width="1080" height="80" viewBox="0 0 1080 80">
  <path d="M32 4 L14 34 L32 64" stroke="#dde6f0" stroke-width="2" fill="none"/>
  <path d="M1048 4 L1066 34 L1048 64" stroke="#dde6f0" stroke-width="2" fill="none"/>
</svg>

<footer class="site-footer">
  <div class="footer-brand">TOLVIRA</div>
  <div class="footer-contact">42 Larkfield Road<br>Suite 210, Brookvale, GA 30999<br>Tel : 470-555-0187<br>E-mail: info@tolvira.example</div>
  <div class="footer-col-title" style="left:440px;top:86px">Company</div>
  <ul class="footer-links"><li>Home</li><li>About Us</li><li>Services</li><li>Team</li><li>Contact Us</li></ul>
  <div class="footer-col-title" style="left:662px;top:82px">NewsLatter</div>
  <div class="abs" style="left:662px;top:116px;font-size:12.5px">Entice shoppers to sign up for your list</div>
  <div class="newsletter-form"><div class="field">Your Email</div><div class="submit">SUBSCRIBE</div></div>
  <div class="social"><span></span><span></span><span></span><span></span><span></span></div>
  <div class="copyright">© 2021 tolvira.example. All rights reserved</div>
</footer>

</body>
</html>
```